"The Wandering Mentor", a Higher Ed blogger, would like a wordpress design

I would like a wordpress design for blogs written by "The Wandering Mentor." that can be easily expanded by me once the initial design is complete.

Here is context which I would like included on the Home/Welcome page: "I started The Wandering Mentor in 2021 to write about the practice of academic advising through the lens of horsemanship. After one year of developing skills as a brand new equestrian, I couldn’t help but notice the similarities between my vocation as an academic advisor and my avocation as a budding equestrian. I hope my musings about my journey in two very different fields will cultivate curiosity, widen your aperture and ignite academic advisors to take their practice to the next level. "

The wordpress will primarily have blogs by myself or guest bloggers writing about academic advising for advisors, but I may widen my audience to include students and families. I'd like to have readers submit questions that I can answer. Depending on interest, I may want to have a section on Horsemanship but that is not truly the focus of this site.

I'd like the feel of the site to be positive, fresh, modern (but not too wild), with the emphasis on Higher Ed/Academic Advising as opposed to equestrian pursuits. I don't want it to feel clunky and blocky like some sites that have to do with education. I'm hoping that readers will have some "aha" moments after reading some of the posts.

I have included my logo files

```html
<!DOCTYPE html>
<html lang="en">
<head>
<meta charset="utf-8">
<title>The Wandering Mentor – Blog Design</title>
<link href="https://fonts.googleapis.com/css2?family=Montserrat:wght@400;500;600;700;800&display=swap" rel="stylesheet">
<style>
:root{
  --gold:#d6ab6b;
  --gold-soft:#c99d5e;
  --black:#000;
  --ink:#0b0b0b;
  --field:#1c1c1c;
  --footer:#1b1b1b;
  --line:#3a3a3a;
  --cream:#f5ece1;
  --white:#fff;
  --text:#1f1f1f;
  --muted:#bfa57a;
}
*{box-sizing:border-box;margin:0;padding:0}
html,body{width:1200px;height:3654px;overflow:hidden}
body{background:var(--white);font-family:'Montserrat',sans-serif;color:var(--text);position:relative}
.abs{position:absolute}
.board-top{position:absolute;left:0;top:0;width:1200px;height:875px;background:var(--white)}
.board-cream{position:absolute;left:0;top:875px;width:1200px;height:2779px;background:var(--cream)}
.brand-ring{position:absolute;border:3px solid #222;border-radius:50%}
.brand-name{position:absolute;font-family:'Montserrat',sans-serif;font-weight:500;color:#222;white-space:nowrap}
.section-title{position:absolute;top:930px;font-weight:800;font-size:30px;color:#111;letter-spacing:.3px;transform:translateX(-50%);white-space:nowrap}

/* screens */
.screen{position:absolute;background:var(--black);overflow:hidden;border-radius:6px}
.photo{position:absolute;display:block}
.photo-office{background:linear-gradient(120deg,#6b5a48 0%,#3d3128 45%,#2a221c 70%,#4a3b2e 100%)}
.photo-horse{background:linear-gradient(180deg,#3f5a35 0%,#56704a 40%,#9b9688 70%,#8f7a5e 100%)}
.photo-laptop{background:linear-gradient(135deg,#d9d1c6 0%,#b7aa98 50%,#8a7c6a 100%)}
.photo-cafe{background:linear-gradient(135deg,#3e3a33 0%,#6f5a44 50%,#a38560 100%)}
.photo-study{background:linear-gradient(135deg,#5d6a7a 0%,#3a3f4a 50%,#b39a3a 100%)}
.photo-rider{background:radial-gradient(circle at 50% 60%,#8a5a34 0%,#4a6a3a 55%,#2c4326 100%)}
.hero-shade{position:absolute;inset:0;background:linear-gradient(180deg,rgba(0,0,0,.35),rgba(0,0,0,.55))}
.hero-curve{position:absolute;left:0;width:100%}
.logo-ring{position:absolute;border:2px solid var(--gold);border-radius:50%}
.logo-name{position:absolute;color:var(--white);font-weight:500;white-space:nowrap;transform:translateX(-50%)}
.hero-title{position:absolute;left:0;width:100%;text-align:center;color:var(--white);font-weight:800;text-transform:uppercase;line-height:1}
.hero-sub{position:absolute;left:0;width:100%;text-align:center;color:#f3e2c4;font-weight:600}
.menu-btn{position:absolute;border:1.5px solid var(--white);border-radius:50%;background:rgba(0,0,0,.3)}
.menu-btn i{position:absolute;left:28%;width:44%;height:1.5px;background:var(--white)}

/* page panels */
.panel{position:absolute;background:var(--black);overflow:hidden}
.widget-title{position:absolute;color:var(--gold);font-weight:500;white-space:nowrap}
.field{position:absolute;background:var(--field);color:#bbb;font-style:italic;display:flex;align-items:center}
.search-btn{position:absolute;background:var(--gold);display:flex;align-items:center;justify-content:center}
.rule{position:absolute;height:1px;background:var(--line)}
.rule-gold{position:absolute;height:1px;background:var(--gold-soft)}
.date-tag{position:absolute;background:var(--gold);color:#1a1a1a;font-weight:500;white-space:nowrap;display:flex;align-items:center;justify-content:center}
.post-title{position:absolute;color:var(--gold);font-weight:500;line-height:1.35}
.post-text{position:absolute;color:#d8c29a;line-height:1.6}
.read-more{position:absolute;color:var(--gold);font-weight:600;text-decoration:underline;white-space:nowrap}
.btn{position:absolute;background:var(--gold);color:#111;font-weight:700;display:flex;align-items:center;justify-content:center}
.pop-item{position:absolute;left:0;width:153px;height:36px}
.pop-thumb{position:absolute;left:0;top:0;width:35px;height:30px}
.pop-text{position:absolute;left:43px;top:0;color:var(--gold);font-size:7.2px;line-height:1.4}
.cat{position:absolute;left:0;color:var(--gold);font-size:7.5px;font-weight:600}
.tag{position:absolute;width:47px;height:15px;border:1px solid #3c3c3c;color:var(--gold);font-size:6.5px;display:flex;align-items:center;justify-content:center}
.social{position:absolute;left:0;display:flex;align-items:center;gap:7px;color:var(--gold);font-size:7px}
.social b{display:block;width:15px;height:15px;border-radius:50%}
.social u{color:#6fa3ff}
.about-title{position:absolute;color:var(--gold);font-weight:400;white-space:nowrap}
.about-text{position:absolute;color:#c7a466;line-height:1.75}
.about-photo{position:absolute;border-radius:50%;border:2px solid #3a3a3a}
.footer-area{position:absolute;left:0;width:100%;background:var(--footer)}
.footer-ring{position:absolute;border-radius:50%;border:2px solid #555;background:#111;display:flex;align-items:center;justify-content:center;color:var(--gold);font-weight:600;text-align:center;line-height:1.2}
.footer-links{position:absolute;left:0;width:100%;text-align:center;color:#e6e6e6}
.copy-bar{position:absolute;left:0;width:100%;background:var(--gold);color:#2a2a2a}
.accordion{position:absolute;left:7px;width:284px;height:24px;border-bottom:1px solid var(--gold-soft);color:var(--gold);font-size:11px;font-weight:500}
.accordion span{position:absolute;right:4px;top:-2px;font-size:14px;font-weight:300}
.mark-name{position:absolute;color:var(--gold);font-weight:600;white-space:nowrap;text-align:center}
</style>
</head>
<body>

<!-- ================= PRESENTATION HEADER ================= -->
<section class="board-top">
  <div class="brand-ring" style="left:552px;top:36px;width:96px;height:96px"></div>
  <div class="brand-name" style="left:0;width:1200px;text-align:center;top:138px;font-size:26px">The Wandering Mentor</div>

  <!-- desktop screen -->
  <div class="screen" style="left:284px;top:227px;width:699px;height:475px">
    <div class="photo photo-office" role="img" aria-label="Photo of two colleagues discussing documents at a desk" style="left:0;top:0;width:699px;height:390px"></div>
    <div class="hero-shade" style="height:390px"></div>
    <svg class="hero-curve" style="top:350px;height:60px" viewBox="0 0 699 60" preserveAspectRatio="none">
      <path d="M0 0 Q350 90 699 0 L699 60 L0 60Z" fill="#000"/>
      <path d="M0 0 Q350 90 699 0" fill="none" stroke="#d6ab6b" stroke-width="2"/>
    </svg>
    <div class="logo-ring" style="left:330px;top:14px;width:40px;height:40px"></div>
    <div class="logo-name" style="left:349px;top:62px;font-size:12px">The Wandering Mentor</div>
    <div class="menu-btn" style="left:580px;top:22px;width:22px;height:22px"><i style="top:35%"></i><i style="top:50%"></i><i style="top:65%"></i></div>
    <div class="hero-title" style="top:180px;font-size:26px">The Wandering<br>Mentor</div>
    <div class="hero-sub" style="top:240px;font-size:12px">Your Partner in Higher Education</div>
    <div class="photo photo-horse" role="img" aria-label="Photo of a rider jumping a white horse" style="left:92px;top:393px;width:265px;height:50px"></div>
    <div class="date-tag" style="left:303px;top:398px;width:50px;height:12px;font-size:7px">13 Sep 2021</div>
    <div class="widget-title" style="left:451px;top:393px;font-size:11px">Search For Blog</div>
    <div class="field" style="left:451px;top:415px;width:128px;height:22px;font-size:8px;padding-left:8px">Search</div>
    <div class="search-btn" style="left:579px;top:415px;width:22px;height:22px"><svg width="10" height="10" viewBox="0 0 10 10"><circle cx="4" cy="4" r="3" fill="none" stroke="#111" stroke-width="1.3"/><path d="M6.2 6.2 9 9" stroke="#111" stroke-width="1.3"/></svg></div>
  </div>

  <!-- tablet screen -->
  <div class="screen" style="left:121px;top:450px;width:224px;height:295px">
    <div class="photo photo-office" role="img" aria-label="Photo of two colleagues discussing documents" style="left:0;top:0;width:224px;height:190px"></div>
    <div class="hero-shade" style="height:190px"></div>
    <svg class="hero-curve" style="top:168px;height:30px" viewBox="0 0 224 30" preserveAspectRatio="none">
      <path d="M0 0 Q112 44 224 0 L224 30 L0 30Z" fill="#000"/>
      <path d="M0 0 Q112 44 224 0" fill="none" stroke="#d6ab6b" stroke-width="1.5"/>
    </svg>
    <div class="logo-ring" style="left:100px;top:8px;width:24px;height:24px"></div>
    <div class="logo-name" style="left:112px;top:36px;font-size:6.5px">The Wandering Mentor</div>
    <div class="menu-btn" style="left:200px;top:8px;width:14px;height:14px"><i style="top:35%"></i><i style="top:50%"></i><i style="top:65%"></i></div>
    <div class="hero-title" style="top:80px;font-size:15px">The Wandering<br>Mentor</div>
    <div class="hero-sub" style="top:116px;font-size:7px">Your Partner in Higher Education</div>
    <div class="widget-title" style="left:16px;top:216px;font-size:8px">Search For Blog</div>
    <div class="field" style="left:16px;top:230px;width:176px;height:20px;font-size:6px;padding-left:8px">Search</div>
    <div class="search-btn" style="left:192px;top:230px;width:20px;height:20px"><svg width="8" height="8" viewBox="0 0 10 10"><circle cx="4" cy="4" r="3" fill="none" stroke="#111" stroke-width="1.3"/><path d="M6.2 6.2 9 9" stroke="#111" stroke-width="1.3"/></svg></div>
    <div class="widget-title" style="left:16px;top:270px;font-size:8px">Popular Posts</div>
    <div class="widget-title" style="left:200px;top:268px;font-size:10px">+</div>
    <div class="rule-gold" style="left:16px;top:266px;width:196px"></div>
    <div class="rule-gold" style="left:16px;top:286px;width:196px"></div>
  </div>

  <!-- phone screen -->
  <div class="screen" style="left:940px;top:490px;width:130px;height:280px">
    <div class="photo photo-office" role="img" aria-label="Photo of two colleagues discussing documents" style="left:0;top:0;width:130px;height:125px"></div>
    <div class="hero-shade" style="height:125px"></div>
    <svg class="hero-curve" style="top:110px;height:20px" viewBox="0 0 130 20" preserveAspectRatio="none">
      <path d="M0 0 Q65 28 130 0 L130 20 L0 20Z" fill="#000"/>
      <path d="M0 0 Q65 28 130 0" fill="none" stroke="#d6ab6b" stroke-width="1"/>
    </svg>
    <div class="logo-ring" style="left:58px;top:14px;width:14px;height:14px"></div>
    <div class="logo-name" style="left:65px;top:31px;font-size:4.5px">The Wandering Mentor</div>
    <div class="menu-btn" style="left:113px;top:14px;width:9px;height:9px"></div>
    <div class="hero-title" style="top:58px;font-size:9px">The Wandering<br>Mentor</div>
    <div class="hero-sub" style="top:80px;font-size:4.3px">Your Partner in Higher Education</div>
    <div class="widget-title" style="left:8px;top:142px;font-size:4.5px">Search For Blog</div>
    <div class="field" style="left:8px;top:150px;width:106px;height:10px;font-size:4px;padding-left:4px">Search</div>
    <div class="search-btn" style="left:114px;top:150px;width:10px;height:10px"></div>
    <div class="widget-title" style="left:8px;top:170px;font-size:4.2px">Popular Posts</div>
    <div class="rule-gold" style="left:8px;top:178px;width:116px"></div>
    <div class="widget-title" style="left:8px;top:184px;font-size:4.2px">Readers Submit Questions</div>
    <div class="rule-gold" style="left:8px;top:192px;width:116px"></div>
    <div class="widget-title" style="left:8px;top:198px;font-size:4.2px">Categories</div>
    <div class="rule-gold" style="left:8px;top:206px;width:116px"></div>
    <div class="widget-title" style="left:8px;top:212px;font-size:4.2px">Tags</div>
    <div class="rule-gold" style="left:8px;top:220px;width:116px"></div>
    <div class="widget-title" style="left:8px;top:226px;font-size:4.2px">Social Connect</div>
    <div class="rule-gold" style="left:8px;top:234px;width:116px"></div>
    <div class="photo photo-horse" role="img" aria-label="Photo of a rider jumping a horse" style="left:8px;top:244px;width:116px;height:36px"></div>
    <div class="date-tag" style="left:98px;top:246px;width:24px;height:6px;font-size:3.3px">13 Sep 2021</div>
  </div>
</section>

<!-- ================= CREAM BOARD ================= -->
<section class="board-cream"></section>
<h2 class="section-title" style="left:434px">Home Desktop Version</h2>
<h2 class="section-title" style="left:969px">Mobile Version</h2>

<!-- ================= DESKTOP PAGE ================= -->
<main class="panel desktop-page" style="left:82px;top:990px;width:705px;height:1841px">
  <header class="hero">
    <div class="photo photo-office" role="img" aria-label="Photo of two colleagues reviewing documents at a desk" style="left:0;top:0;width:705px;height:352px"></div>
    <div class="hero-shade" style="height:352px"></div>
    <svg class="hero-curve" style="top:300px;height:60px" viewBox="0 0 705 60" preserveAspectRatio="none">
      <path d="M0 0 Q352 90 705 0 L705 60 L0 60Z" fill="#000"/>
      <path d="M0 0 Q352 90 705 0" fill="none" stroke="#d6ab6b" stroke-width="2"/>
    </svg>
    <div class="logo-ring" style="left:330px;top:8px;width:44px;height:44px"></div>
    <div class="logo-name" style="left:352px;top:56px;font-size:13px">The Wandering Mentor</div>
    <div class="menu-btn" style="left:589px;top:17px;width:22px;height:22px"><i style="top:35%"></i><i style="top:50%"></i><i style="top:65%"></i></div>
    <h1 class="hero-title" style="top:177px;font-size:27px">The Wandering<br>Mentor</h1>
    <p class="hero-sub" style="top:238px;font-size:12.5px">Your Partner in Higher Education</p>
  </header>

  <!-- posts -->
  <article>
    <div class="photo photo-horse" role="img" aria-label="Photo of a rider jumping a white horse over a fence" style="left:94px;top:396px;width:329px;height:167px"></div>
    <div class="date-tag" style="left:362px;top:400px;width:56px;height:14px;font-size:7.5px">13 Sep 2021</div>
    <h3 class="post-title" style="left:94px;top:575px;width:329px;font-size:13px">Lorem Ipsum Is Simply Dummy Text Of Printing And Typesetting Industry</h3>
    <p class="post-text" style="left:94px;top:617px;width:329px;font-size:7.5px">Lorem Ipsum is simply dummy text of the printing and typesetting industry. Lorem Ipsum has been the industry's standard dummy text ever since the 1500s, when an unknown printer took a galley of type and scrambled</p>
    <a class="read-more" style="left:94px;top:670px;font-size:9px">Continue Reading</a>
  </article>
  <div class="rule" style="left:94px;top:705px;width:329px"></div>

  <article>
    <div class="photo photo-laptop" role="img" aria-label="Photo of two women working at a laptop" style="left:94px;top:736px;width:154px;height:121px"></div>
    <div class="date-tag" style="left:190px;top:740px;width:54px;height:13px;font-size:7px">13 Sep 2021</div>
    <h3 class="post-title" style="left:94px;top:869px;width:154px;font-size:7.5px">Lorem Ipsum Is Simply Dummy Text Of Printing And Typesetting...</h3>
    <p class="post-text" style="left:94px;top:893px;width:154px;font-size:6.5px">Lorem Ipsum is simply dummy text of the printing and typesetting industry...</p>
    <a class="read-more" style="left:94px;top:929px;font-size:7px">Continue Reading</a>
  </article>
  <article>
    <div class="photo photo-cafe" role="img" aria-label="Photo of students studying together at a cafe table" style="left:270px;top:736px;width:153px;height:121px"></div>
    <div class="date-tag" style="left:365px;top:740px;width:54px;height:13px;font-size:7px">13 Sep 2021</div>
    <h3 class="post-title" style="left:270px;top:869px;width:153px;font-size:7.5px">Lorem Ipsum Is Simply Dummy Text Of Printing And Typesetting...</h3>
    <p class="post-text" style="left:270px;top:893px;width:153px;font-size:6.5px">Lorem Ipsum is simply dummy text of the printing and typesetting industry...</p>
    <a class="read-more" style="left:270px;top:929px;font-size:7px">Continue Reading</a>
  </article>
  <div class="rule" style="left:94px;top:967px;width:329px"></div>

  <article>
    <div class="date-tag" style="left:94px;top:996px;width:56px;height:14px;font-size:7.5px">13 Sep 2021</div>
    <h3 class="post-title" style="left:94px;top:1020px;width:329px;font-size:13px">Lorem Ipsum Is Simply Dummy Text Of Printing And Typesetting Industry</h3>
    <p class="post-text" style="left:94px;top:1063px;width:329px;font-size:7.5px">Lorem Ipsum is simply dummy text of the printing and typesetting industry. Lorem Ipsum has been the industry's standard dummy text ever since the 1500s, when an unknown printer took a galley of type and scrambled</p>
    <a class="read-more" style="left:94px;top:1116px;font-size:9px">Continue Reading</a>
  </article>
  <div class="rule" style="left:94px;top:1155px;width:329px"></div>

  <article>
    <div class="photo photo-study" role="img" aria-label="Photo of two students smiling over a notebook" style="left:94px;top:1183px;width:154px;height:121px"></div>
    <div class="date-tag" style="left:270px;top:1194px;width:54px;height:13px;font-size:7px">13 Sep 2021</div>
    <h3 class="post-title" style="left:270px;top:1214px;width:153px;font-size:7.5px">Lorem Ipsum Is Simply Dummy Text Of Printing And Typesetting...</h3>
    <p class="post-text" style="left:270px;top:1240px;width:153px;font-size:6.5px">Lorem ipsum is simply dummy text of the printing and typesetting industry...</p>
    <a class="read-more" style="left:270px;top:1276px;font-size:7px">Continue Reading</a>
  </article>
  <div class="btn" style="left:94px;top:1338px;width:84px;height:25px;font-size:8.5px">Load More</div>

  <!-- sidebar -->
  <aside class="sidebar abs" style="left:457px;top:0;width:153px;height:1400px">
    <h4 class="widget-title" style="left:0;top:393px;font-size:11px">Search For Blog</h4>
    <div class="field" style="left:0;top:414px;width:125px;height:23px;font-size:7px;padding-left:8px">Search</div>
    <div class="search-btn" style="left:125px;top:414px;width:28px;height:23px"><svg width="10" height="10" viewBox="0 0 10 10"><circle cx="4" cy="4" r="3" fill="none" stroke="#111" stroke-width="1.3"/><path d="M6.2 6.2 9 9" stroke="#111" stroke-width="1.3"/></svg></div>
    <div class="rule" style="left:0;top:457px;width:153px;background:#666"></div>

    <h4 class="widget-title" style="left:0;top:472px;font-size:11px">Popular Posts</h4>
    <div class="pop-item" style="top:500px"><div class="pop-thumb photo-study" role="img" aria-label="Post thumbnail photo"></div><p class="pop-text">Lorem ipsum tex printing<br>and typesetting...<br>13 Sep 2021</p></div>
    <div class="rule" style="left:0;top:541px;width:153px"></div>
    <div class="pop-item" style="top:548px"><div class="pop-thumb photo-horse" role="img" aria-label="Post thumbnail photo"></div><p class="pop-text">Lorem ipsum tex printing<br>and typesetting...<br>13 Sep 2021</p></div>
    <div class="rule" style="left:0;top:589px;width:153px"></div>
    <div class="pop-item" style="top:596px"><div class="pop-thumb photo-laptop" role="img" aria-label="Post thumbnail photo"></div><p class="pop-text">Lorem ipsum tex printing<br>and typesetting...<br>13 Sep 2021</p></div>
    <div class="rule" style="left:0;top:637px;width:153px"></div>
    <div class="pop-item" style="top:644px"><div class="pop-thumb photo-cafe" role="img" aria-label="Post thumbnail photo"></div><p class="pop-text">Lorem ipsum tex printing<br>and typesetting...<br>13 Sep 2021</p></div>
    <div class="rule" style="left:0;top:690px;width:153px;background:#666"></div>

    <h4 class="widget-title" style="left:0;top:703px;font-size:11px">Readers Submit Questions</h4>
    <div class="field" style="left:0;top:723px;width:153px;height:23px;font-size:6px;font-style:normal;color:#ccc;padding-left:6px">Email Address</div>
    <div class="field" style="left:0;top:752px;width:153px;height:28px;font-size:6px;font-style:normal;color:#ccc;padding-left:6px;align-items:flex-start;padding-top:7px">Submit Your Questions</div>
    <div class="btn" style="left:0;top:790px;width:153px;height:21px;font-size:9.5px;font-weight:600">Post Question</div>
    <div class="rule" style="left:0;top:820px;width:153px;background:#666"></div>

    <h4 class="widget-title" style="left:0;top:828px;font-size:11px">Categories</h4>
    <div class="cat" style="top:850px">» Education</div>
    <div class="cat" style="top:868px">» Academic</div>
    <div class="cat" style="top:886px">» Consulting</div>
    <div class="cat" style="top:904px">» Advisor</div>
    <div class="cat" style="top:922px">» Business</div>
    <div class="rule" style="left:0;top:950px;width:153px;background:#666"></div>

    <h4 class="widget-title" style="left:0;top:968px;font-size:11px">Tags</h4>
    <div class="tag" style="left:0;top:992px">Education</div><div class="tag" style="left:53px;top:992px">Academic</div><div class="tag" style="left:106px;top:992px">Consulting</div>
    <div class="tag" style="left:0;top:1013px">Lorem Ipsum</div><div class="tag" style="left:53px;top:1013px">Advisor</div><div class="tag" style="left:106px;top:1013px">Business</div>
    <div class="tag" style="left:0;top:1033px">Education</div><div class="tag" style="left:53px;top:1033px">Academic</div><div class="tag" style="left:106px;top:1033px">Consulting</div>
    <div class="tag" style="left:0;top:1054px">Lorem Ipsum</div><div class="tag" style="left:53px;top:1054px">Advisor</div><div class="tag" style="left:106px;top:1054px">Business</div>
    <div class="rule" style="left:0;top:1087px;width:153px;background:#666"></div>

    <h4 class="widget-title" style="left:0;top:1106px;font-size:11px">Social Connect</h4>
    <div class="social" style="top:1132px"><b style="background:#3b5fb0"></b>Follow us on <u>Circlebook</u></div>
    <div class="social" style="top:1156px"><b style="background:#3aa3e8"></b>Follow us on <u>Chirper</u></div>
    <div class="social" style="top:1180px"><b style="background:#e0262c"></b>Subscribe <u style="color:#e05555">Streamtube</u></div>
    <div class="social" style="top:1204px"><b style="background:#b63cc0"></b>Follow us on <u style="color:#c05ad0">Snapgram</u></div>
    <div class="rule" style="left:0;top:1237px;width:153px;background:#666"></div>
    <div class="mark-name" style="left:0;top:1285px;width:153px;font-size:15px">The Wandering<br>Mentor</div>
  </aside>

  <!-- about -->
  <section class="about">
    <div class="about-photo photo-rider" role="img" aria-label="Photo of a rider on a chestnut horse" style="left:101px;top:1429px;width:192px;height:192px"></div>
    <h2 class="about-title" style="left:315px;top:1452px;font-size:21px">The Wandering Mentor</h2>
    <p class="about-text" style="left:315px;top:1486px;width:278px;font-size:6.9px">We started The Wandering Mentor in 2021 to write about the practice of academic advising through the lens of horsemanship. After one year of developing skills as a brand new equestrian, we couldn't help but notice the similarities between our vocation as an academic advisor and my avocation as a budding equestrian.<br><br style="line-height:.4">We hope our musings about our journey in two very different fields will cultivate curiosity, widen your aperture and ignite academic advisors to take their practice to the next level.</p>
  </section>

  <!-- footer -->
  <footer>
    <div class="footer-area" style="top:1640px;height:201px"></div>
    <svg class="abs" style="left:0;top:1630px;width:705px;height:50px" viewBox="0 0 705 50" preserveAspectRatio="none">
      <path d="M0 0 L705 0 L705 10 Q352 70 0 10Z" fill="#000"/>
    </svg>
    <div class="footer-ring" style="left:311px;top:1676px;width:80px;height:80px;font-size:8px">The<br>Wandering<br>Mentor</div>
    <nav class="footer-links" style="top:1781px;font-size:7.5px">Home &nbsp;|&nbsp; Posts &nbsp;Advisor Spotlight &nbsp;|&nbsp; About Wandering Mentor &nbsp;|&nbsp; Advisor Tips &nbsp;|&nbsp; Contact</nav>
    <div class="copy-bar" style="top:1815px;height:26px;font-size:7.5px">
      <span class="abs" style="left:94px;top:8px">Copyright © 2021 <b>The Wandering Mentor</b>. All Rights Reserved.</span>
      <span class="abs" style="left:493px;top:8px">Privacy Policy &nbsp;&nbsp;|&nbsp;&nbsp; Disclaimer</span>
    </div>
  </footer>
</main>

<!-- ================= MOBILE PAGE ================= -->
<main class="panel mobile-page" style="left:818px;top:990px;width:301px;height:2545px">
  <header class="hero">
    <div class="photo photo-office" role="img" aria-label="Photo of two colleagues reviewing documents at a desk" style="left:0;top:0;width:301px;height:265px"></div>
    <div class="hero-shade" style="height:265px"></div>
    <svg class="hero-curve" style="top:235px;height:40px" viewBox="0 0 301 40" preserveAspectRatio="none">
      <path d="M0 0 Q150 50 301 0 L301 40 L0 40Z" fill="#000"/>
      <path d="M0 0 Q150 50 301 0" fill="none" stroke="#d6ab6b" stroke-width="1.5"/>
    </svg>
    <div class="logo-ring" style="left:134px;top:12px;width:32px;height:32px"></div>
    <div class="logo-name" style="left:150px;top:44px;font-size:9px">The Wandering Mentor</div>
    <div class="menu-btn" style="left:268px;top:14px;width:20px;height:20px"><i style="top:35%"></i><i style="top:50%"></i><i style="top:65%"></i></div>
    <h1 class="hero-title" style="top:107px;font-size:22px">The Wandering<br>Mentor</h1>
    <p class="hero-sub" style="top:160px;font-size:10.5px">Your Partner in Higher Education</p>
  </header>

  <h4 class="widget-title" style="left:7px;top:296px;font-size:11px">Search For Blog</h4>
  <div class="field" style="left:7px;top:316px;width:255px;height:29px;font-size:9px;padding-left:12px">Search</div>
  <div class="search-btn" style="left:262px;top:316px;width:29px;height:29px"><svg width="11" height="11" viewBox="0 0 10 10"><circle cx="4" cy="4" r="3" fill="none" stroke="#111" stroke-width="1.3"/><path d="M6.2 6.2 9 9" stroke="#111" stroke-width="1.3"/></svg></div>
  <div class="rule-gold" style="left:7px;top:354px;width:284px"></div>

  <div class="accordion" style="top:367px">Popular Posts<span>+</span></div>
  <div class="accordion" style="top:403px">Readers Submit Questions<span>+</span></div>
  <div class="accordion" style="top:439px">Categories<span>+</span></div>
  <div class="accordion" style="top:475px">Tags<span>+</span></div>
  <div class="accordion" style="top:511px">Social Connect<span>+</span></div>

  <article>
    <div class="photo photo-horse" role="img" aria-label="Photo of a rider jumping a white horse over a fence" style="left:7px;top:570px;width:284px;height:142px"></div>
    <div class="date-tag" style="left:231px;top:575px;width:56px;height:14px;font-size:7.5px">13 Sep 2021</div>
    <h3 class="post-title" style="left:10px;top:726px;width:280px;font-size:10.5px">Lorem Ipsum Is Simply Dummy Text Of Printing And Typesetting Industry</h3>
    <p class="post-text" style="left:10px;top:761px;width:280px;font-size:8.3px;line-height:1.95">Lorem Ipsum is simply dummy text of the printing and typesetting industry. Lorem Ipsum has been the industry's standard dummy text ever since the 1500s, when an unknown printer took a galley of type and scrambled</p>
    <a class="read-more" style="left:10px;top:837px;font-size:8.5px;text-decoration:none">Continue Reading</a>
  </article>
  <article>
    <div class="photo photo-laptop" role="img" aria-label="Photo of two women working at a laptop" style="left:7px;top:894px;width:284px;height:141px"></div>
    <div class="date-tag" style="left:231px;top:899px;width:56px;height:14px;font-size:7.5px">13 Sep 2021</div>
    <h3 class="post-title" style="left:10px;top:1050px;width:280px;font-size:10.5px">Lorem Ipsum Is Simply Dummy Text Of Printing And Typesetting...</h3>
    <p class="post-text" style="left:10px;top:1085px;width:280px;font-size:8.3px;line-height:1.95">Lorem Ipsum is simply dummy text of the printing and typesetting industry. Lorem Ipsum has been the industry's standard dummy</p>
    <a class="read-more" style="left:10px;top:1144px;font-size:8.5px;text-decoration:none">Continue Reading</a>
  </article>
  <article>
    <div class="photo photo-cafe" role="img" aria-label="Photo of students studying together at a cafe table" style="left:7px;top:1172px;width:284px;height:142px"></div>
    <div class="date-tag" style="left:231px;top:1177px;width:56px;height:14px;font-size:7.5px">13 Sep 2021</div>
    <h3 class="post-title" style="left:10px;top:1328px;width:280px;font-size:10.5px">Lorem Ipsum Is Simply Dummy Text Of Printing And Typesetting...</h3>
    <p class="post-text" style="left:10px;top:1363px;width:280px;font-size:8.3px;line-height:1.95">Lorem Ipsum is simply dummy text of the printing and typesetting industry. Lorem Ipsum has been the industry's standard dummy</p>
    <a class="read-more" style="left:10px;top:1422px;font-size:8.5px;text-decoration:none">Continue Reading</a>
  </article>
  <article>
    <div class="date-tag" style="left:7px;top:1480px;width:56px;height:15px;font-size:7.5px">13 Sep 2021</div>
    <h3 class="post-title" style="left:10px;top:1507px;width:280px;font-size:10.5px">Lorem Ipsum Is Simply Dummy Text Of Printing And Typesetting Industry</h3>
    <p class="post-text" style="left:10px;top:1542px;width:280px;font-size:8.3px;line-height:1.95">Lorem Ipsum is simply dummy text of the printing and typesetting industry. Lorem Ipsum has been the industry's standard dummy text ever since the 1500s, when an unknown printer took a galley of type and scrambled</p>
    <a class="read-more" style="left:10px;top:1617px;font-size:8.5px;text-decoration:none">Continue Reading</a>
  </article>
  <article>
    <div class="photo photo-study" role="img" aria-label="Photo of two students smiling over a notebook" style="left:7px;top:1674px;width:130px;height:127px"></div>
    <div class="date-tag" style="left:151px;top:1681px;width:56px;height:14px;font-size:7.5px">13 Sep 2021</div>
    <h3 class="post-title" style="left:151px;top:1701px;width:140px;font-size:10.5px">Lorem Ipsum Is Simply Dummy Text Of...</h3>
    <p class="post-text" style="left:151px;top:1733px;width:140px;font-size:8.3px;line-height:1.95">Lorem Ipsum is simply dummy text of the printing and typesetting industry...</p>
    <a class="read-more" style="left:151px;top:1790px;font-size:8.5px;text-decoration:none">Continue Reading</a>
  </article>
  <div class="btn" style="left:108px;top:1828px;width:82px;height:24px;font-size:10px">Load More</div>

  <section class="about">
    <h2 class="about-title" style="left:0;width:301px;text-align:center;top:1884px;font-size:17px">The Wandering Mentor</h2>
    <div class="about-photo photo-rider" role="img" aria-label="Photo of a rider on a chestnut horse" style="left:49px;top:1915px;width:204px;height:204px"></div>
    <p class="about-text" style="left:12px;top:2132px;width:277px;font-size:8.6px;text-align:center;line-height:1.95">We started The Wandering Mentor in 2021 to write about the practice of academic advising through the lens of horsemanship. After one year of developing skills as a brand new equestrian, we couldn't help but notice the similarities between our vocation as an academic advisor and my avocation as a budding equestrian.<br><br style="line-height:.4">We hope our musings about our journey in two very different fields will cultivate curiosity, widen your aperture and ignite academic advisors to take their practice to the next level.</p>
  </section>

  <footer>
    <div class="footer-area" style="top:2325px;height:220px"></div>
    <svg class="abs" style="left:0;top:2318px;width:301px;height:30px" viewBox="0 0 301 30" preserveAspectRatio="none">
      <path d="M0 0 L301 0 L301 6 Q150 40 0 6Z" fill="#000"/>
    </svg>
    <div class="footer-ring" style="left:109px;top:2327px;width:84px;height:84px;font-size:8.5px">The<br>Wandering<br>Mentor</div>
    <nav class="footer-links" style="top:2432px;font-size:8.5px;line-height:2.2">Home &nbsp;| &nbsp;Posts &nbsp;Advisor Spotlight &nbsp;| &nbsp;About Wandering<br>Mentor &nbsp;| &nbsp;Advisor Tips &nbsp;| &nbsp;Contact</nav>
    <div class="copy-bar" style="top:2482px;height:63px;font-size:8.3px;text-align:center;line-height:1.3">
      <div style="padding-top:12px">Privacy Policy &nbsp;&nbsp;|&nbsp;&nbsp; Disclaimer</div>
      <div style="padding-top:5px">Copyright © 2021 <b>The Wandering Mentor</b>.<br>All Rights Reserved.</div>
    </div>
  </footer>
</main>

<!-- ================= LARGE MARK ================= -->
<div class="brand-ring" style="left:330px;top:3115px;width:34px;height:34px;border-color:#1a1a1a;border-width:2px;background:#1a1a1a"></div>
<div class="brand-name" style="left:380px;top:3105px;font-size:44px;color:var(--gold);font-weight:600;line-height:1.15">The Wandering<br>Mentor</div>

</body>
</html>
```